Chestnut Farm Logo and Business Card

We need a new logo design and new business cards for a recently purchased mature Chestnut Farm in the south west of Western Australia, the farm is called Willowmere Glen, We will be adding value to the chestnuts by creating a range of chestnut products based on the fact that chestnuts are a healthy, gluten free product that is suited to the vegetarian market as well as the health food market. We will be selling the products through farmers markets, restaurants, health food stores and online. The final design should communicate a healthy modern down to earth image.
Updates

Sorry, I should have given the details for the business cards.

Address is 
Willowmere Glen
PO Box 417 
Brookvale, South Westland, 6382

Email is 
willowmere.glen@fernmail.example

Website is
www.glenorchardwa.example

Phone number is 
(08) 9413 2870

Many thanks

We would like to see the logo separate to the business card as well if possible please?

Industry/Entity Type

Farm

Logo Text

Willowmere Glen

```html
<!DOCTYPE html>
<html lang="en">
<head>
<meta charset="utf-8">
<title>Willowmere Glen – Logo and Business Cards</title>
<link rel="stylesheet" href="https://fonts.googleapis.com/css2?family=Arimo:wght@400;700&display=swap">
<style>
  :root {
    --backdrop: #d6d6d6;
    --maroon: #7a2f2c;
    --leaf-green: #4caa4c;
    --white: #ffffff;
    --ink-soft: #f4f4f4;
  }
  * { box-sizing: border-box; margin: 0; padding: 0; }
  html, body { width: 1200px; height: 874px; overflow: hidden; }
  body {
    background: var(--backdrop);
    font-family: "Arimo", Arial, sans-serif;
    position: relative;
  }

  /* Standalone logo */
  .brand-logo {
    position: absolute;
    left: 40px; top: 60px;
    display: flex; flex-direction: column; align-items: center; gap: 14px;
    width: 340px;
  }
  .brand-logo .mark-dot {
    width: 150px; height: 150px; border-radius: 50%;
    background: var(--maroon);
  }
  .brand-name {
    font-weight: 700;
    text-transform: uppercase;
    letter-spacing: 0.5px;
    color: var(--maroon);
    white-space: nowrap;
  }
  .brand-logo .brand-name { font-size: 30px; }

  /* Cards */
  .card {
    position: absolute;
    width: 580px; height: 354px;
    border-radius: 4px;
    box-shadow: 0 6px 14px rgba(0,0,0,0.22);
  }

  .card-back {
    left: 560px; top: 70px;
    background: var(--maroon);
    display: flex; flex-direction: column; align-items: center; justify-content: center; gap: 26px;
  }
  .card-back .mark-dot {
    width: 140px; height: 140px; border-radius: 50%;
    background: var(--white);
  }
  .card-back .brand-name { color: var(--white); font-size: 46px; }

  .card-front {
    left: 140px; top: 460px;
    background: var(--leaf-green);
    color: var(--white);
  }
  .card-front .front-logo {
    position: absolute; left: 34px; top: 32px;
    display: flex; align-items: center; gap: 10px;
  }
  .card-front .mark-dot {
    width: 36px; height: 36px; border-radius: 50%;
    background: var(--maroon);
  }
  .card-front .brand-name { font-size: 17px; }

  .postal-address {
    position: absolute; right: 34px; top: 78px;
    text-align: right; font-style: normal;
    font-weight: 700; font-size: 17px; line-height: 1.35;
  }

  .contact-lines {
    position: absolute; left: 0; right: 0; top: 150px;
    display: flex; flex-direction: column; align-items: center; gap: 8px;
    font-size: 24px; color: var(--ink-soft);
  }
  .contact-lines .icon { width: 28px; height: 28px; display: block; }
</style>
</head>
<body>

  <div class="brand-logo">
    <span class="mark-dot"></span>
    <span class="brand-name">Willowmere Glen</span>
  </div>

  <section class="card card-back" aria-label="Business card, back">
    <span class="mark-dot"></span>
    <span class="brand-name">Willowmere Glen</span>
  </section>

  <section class="card card-front" aria-label="Business card, front">
    <div class="front-logo">
      <span class="mark-dot"></span>
      <span class="brand-name">Willowmere Glen</span>
    </div>

    <address class="postal-address">
      PO Box 417<br>
      Brookvale, South Westland<br>
      6382
    </address>

    <div class="contact-lines">
      <svg class="icon" viewBox="0 0 28 28" aria-hidden="true">
        <rect x="3" y="7" width="22" height="15" fill="none" stroke="#fff" stroke-width="2"/>
        <polyline points="3,7 14,16 25,7" fill="none" stroke="#fff" stroke-width="2"/>
      </svg>
      <span class="contact-email">willowmere.glen@fernmail.example</span>
      <svg class="icon" viewBox="0 0 28 28" aria-hidden="true">
        <path d="M9 3 L9 22 L13 18 L16 25 L19 24 L16 17 L22 17 Z" fill="none" stroke="#fff" stroke-width="2" stroke-linejoin="round"/>
      </svg>
      <span class="contact-web">www.glenorchardwa.example</span>
    </div>
  </section>

</body>
</html>
```